High Quality Business card for Property Management Agency - Super Classy and professional design

High Quality Business card design.

We need a business card designed for our Property Management Agency.
We are located on Sydney's Northern Beaches and manage beautiful properties along the beach and harbor.
We need a design that oozes modern, classy and professional.
I would like it to be double sided with contact details and logo on the front and just the logo on the back.

I need a print ready PDF version of the file as well as an editable photoshop (PSD) version of the file.

Logo and information details attached.

Target Market(s)

Property owners/investors, Male and Female Aged 28-65

Industry/Entity Type

Real Estate

Contact Information for Business Card

Tom Carrick
Tel: 0467 239 018
Email: tom@harvestlaneestates.com.au
Website: www.harvestlaneestates.com.au
Address: Level 2, 17 Wattlecourt Rd, Dunmarra NSW 2187

Font styles to use
Sans Serif

Requirements
Must have
• - Logo front and back
• - Business card details listed above and attached
• - Colour
Nice to have
• Sleek and professional

```html
<!DOCTYPE html>
<html lang="en">
<head>
<meta charset="UTF-8">
<title>Harvest Lane Estates — Business Card</title>
<link href="https://fonts.googleapis.com/css2?family=Roboto:wght@400;500;700&display=swap" rel="stylesheet">
<style>
  :root {
    --bg: #e9e6e1;
    --card-white: #f7f7f7;
    --card-dark: #151b1f;
    --ink: #1b2226;
    --ink-soft: #3a4247;
    --teal: #1f9aab;
    --white: #ffffff;
  }
  * { margin: 0; padding: 0; box-sizing: border-box; }
  html, body { width: 1200px; height: 1023px; overflow: hidden; }
  body {
    background: var(--bg);
    font-family: "Roboto", sans-serif;
    position: relative;
  }
  .card {
    position: absolute;
    left: 220px;
    width: 760px;
    height: 434px;
    border-radius: 22px;
    overflow: hidden;
    box-shadow: 0 10px 30px rgba(0,0,0,0.18);
  }
  .card-front { top: 60px; background: var(--card-white); }
  .card-back  { top: 530px; background: var(--card-dark); }

  .brand {
    position: absolute;
    display: flex;
    align-items: center;
    gap: 14px;
    font-weight: 500;
    letter-spacing: 1px;
    text-transform: uppercase;
    white-space: nowrap;
  }
  .brand-mark { border-radius: 50%; flex: none; }
  .card-front .brand { right: 48px; top: 52px; color: var(--ink); font-size: 40px; }
  .card-front .brand-mark { width: 26px; height: 26px; background: var(--teal); }
  .card-back .brand { left: 50%; top: 150px; transform: translateX(-50%); color: var(--white); font-size: 56px; }
  .card-back .brand-mark { width: 34px; height: 34px; background: var(--teal); }

  .holder-name {
    position: absolute;
    left: 56px; top: 190px;
    color: var(--teal);
    font-weight: 700;
    font-size: 34px;
  }
  .contact-list {
    position: absolute;
    left: 60px; top: 250px;
    list-style: none;
    color: var(--ink-soft);
    font-size: 17px;
    line-height: 1.25;
  }
  .contact-list li { display: flex; align-items: flex-start; gap: 16px; margin-bottom: 8px; }
  .contact-list svg { width: 18px; height: 18px; flex: none; margin-top: 1px; }

  .edge-band {
    position: absolute;
    left: 0; right: 0; bottom: 0;
    height: 26px;
    display: flex;
  }
  .edge-band .teal { width: 46%; background: var(--teal); }
  .edge-band .dark { flex: 1; background: var(--card-dark); }

  .back-web {
    position: absolute;
    left: 50%; top: 300px;
    transform: translateX(-50%);
    color: #d9dde0;
    font-size: 17px;
    letter-spacing: 1px;
  }
</style>
</head>
<body>

<section class="card card-front">
  <div class="brand"><span class="brand-mark"></span>Harvest Lane Estates</div>

  <h1 class="holder-name">Tom Carrick</h1>

  <ul class="contact-list">
    <li>
      <svg viewBox="0 0 24 24" fill="#1f9aab"><path d="M6.6 10.8a15 15 0 006.6 6.6l2.2-2.2a1 1 0 011-.25 11.4 11.4 0 003.6.57 1 1 0 011 1V20a1 1 0 01-1 1A17 17 0 013 4a1 1 0 011-1h3.5a1 1 0 011 1c0 1.25.2 2.45.57 3.57a1 1 0 01-.25 1z"/></svg>
      0467 239 018
    </li>
    <li>
      <svg viewBox="0 0 24 24" fill="none" stroke="#1f9aab" stroke-width="1.8"><rect x="3" y="5" width="18" height="14" rx="1"/><path d="M3 6l9 7 9-7"/></svg>
      tom@harvestlaneestates.com.au
    </li>
    <li>
      <svg viewBox="0 0 24 24" fill="none" stroke="#1f9aab" stroke-width="1.6"><circle cx="12" cy="12" r="9"/><path d="M3 12h18M12 3c3 3 3 15 0 18M12 3c-3 3-3 15 0 18"/></svg>
      www.harvestlaneestates.com.au
    </li>
    <li>
      <svg viewBox="0 0 24 24" fill="#1f9aab"><path d="M12 2a7 7 0 00-7 7c0 5 7 13 7 13s7-8 7-13a7 7 0 00-7-7zm0 9.5A2.5 2.5 0 1112 6.5a2.5 2.5 0 010 5z"/></svg>
      <span>Level 2, 17 Wattlecourt Rd,<br>Dunmarra NSW 2187</span>
    </li>
  </ul>

  <div class="edge-band"><span class="teal"></span><span class="dark"></span></div>
</section>

<section class="card card-back">
  <div class="brand"><span class="brand-mark"></span>Harvest Lane Estates</div>
  <p class="back-web">www.harvestlaneestates.com.au</p>
</section>

</body>
</html>
```